Brightfold Tamaru needs a new label design for our Kombucha range- 5 Flavours

We need a label design for our Kombucha range. We are looking for a new look that says quality, vibrant, modern, energetic. The design should draw from our brand identity and the Zanzibar landscape, while communicating internationally. We need a label that describes us and catches the consumer's eye as they scan the supermarket shelves.
Each label should have the same design foundation- with a slight difference in colour to reflect the Kombucha Flavour. Our flavours are: Classic, Ginger/Turmeric, Hibiscus, Cinammon/Clove and Lemongrass.
I have attached in order: our current label (all info on label will remain the same), screenshots from our brand book, some images of labels we love. Our kombucha is packed in glass bottles- it may be nice to play with clear cut outs that bring out the colour of the beverage within the label design.
Check us out on Instagram @brightfoldtamaru for the vibe

```html
<!DOCTYPE html>
<html lang="en">
<head>
<meta charset="utf-8">
<title>Brightfold Tamaru Kombucha Labels</title>
<link href="https://fonts.googleapis.com/css2?family=Chewy&family=Roboto:wght@400;700&display=swap" rel="stylesheet">
<style>
  :root {
    --page: #f3f0b8;
    --silver-light: #f4f4f4;
    --silver-dark: #b9b9c0;
    --ink: #2a1410;
    --white: #ffffff;
    --green-a: #5fd11a; --green-b: #1f7a0c;
    --purple-a: #b23ad8; --purple-b: #4a1270;
    --red-a: #e0185a; --red-b: #5a0a1c;
    --yellow-a: #e6e21e; --yellow-b: #6f6a0a;
    --blue-a: #2b3fd8; --blue-b: #101a6a;
  }
  html, body {
    margin: 0;
    width: 1200px;
    height: 900px;
    overflow: hidden;
    background: var(--page);
  }
  .label-range {
    display: flex;
    gap: 20px;
    justify-content: center;
    align-items: center;
    height: 900px;
  }
  .label {
    width: 216px;
    height: 440px;
    display: flex;
    flex-direction: column;
    box-shadow: 0 8px 22px rgba(80, 70, 10, 0.18);
  }
  .label--green  { --a: var(--green-a);  --b: var(--green-b); }
  .label--purple { --a: var(--purple-a); --b: var(--purple-b); }
  .label--red    { --a: var(--red-a);    --b: var(--red-b); }
  .label--yellow { --a: var(--yellow-a); --b: var(--yellow-b); }
  .label--blue   { --a: var(--blue-a);   --b: var(--blue-b); }

  .pattern-band {
    height: 46px;
    background: linear-gradient(180deg, var(--silver-light), var(--silver-dark) 55%, var(--silver-light));
  }
  .pattern-band--bottom {
    height: 18px;
    background: linear-gradient(90deg, var(--a), var(--b), var(--a));
    filter: brightness(1.15);
  }
  .label-body {
    flex: 1;
    background: linear-gradient(160deg, var(--a) 0%, var(--b) 100%);
    display: flex;
    flex-direction: column;
    align-items: center;
    padding-top: 14px;
    font-family: "Roboto", Arial, sans-serif;
    color: var(--white);
  }
  .brand-mark {
    display: flex;
    align-items: center;
    gap: 6px;
    background: var(--white);
    color: var(--ink);
    border-radius: 6px;
    padding: 5px 9px;
    font-family: "Chewy", cursive;
    font-size: 15px;
    line-height: 1;
  }
  .brand-mark__dot {
    width: 10px;
    height: 10px;
    border-radius: 50%;
    background: var(--ink);
  }
  .product-name {
    margin: 16px 0 0;
    font-family: "Chewy", cursive;
    font-weight: 400;
    font-size: 74px;
    line-height: 0.82;
    text-align: center;
    color: var(--white);
    -webkit-text-stroke: 5px var(--ink);
    paint-order: stroke fill;
    letter-spacing: -1px;
  }
  .product-name span { display: block; }
  .taglines {
    display: flex;
    justify-content: space-between;
    width: 190px;
    margin-top: 20px;
    font-size: 9px;
    font-weight: 700;
    font-style: italic;
    text-transform: uppercase;
  }
  .flavour {
    margin-top: 8px;
    font-size: 20px;
  }
  .descriptor {
    font-size: 10px;
    margin-top: 2px;
  }
  .volume-row {
    display: flex;
    align-items: center;
    justify-content: center;
    gap: 22px;
    width: 100%;
    margin-top: 16px;
  }
  .volume {
    font-size: 17px;
    font-weight: 700;
  }
  .cert-badge {
    width: 20px;
    height: 20px;
    border-radius: 3px;
    background: var(--white);
  }
</style>
</head>
<body>
<main class="label-range">
  <article class="label label--green">
    <div class="pattern-band" role="img" aria-label="Silver band with Zanzibar-inspired geometric pattern"></div>
    <div class="label-body">
      <div class="brand-mark"><span class="brand-mark__dot"></span>Brightfold Tamaru</div>
      <h2 class="product-name"><span>Komb</span><span>ucha</span></h2>
      <div class="taglines"><span>Feed your body</span><span>Feed your mind</span></div>
      <div class="flavour">Lemongrass</div>
      <div class="descriptor">Natural Soda</div>
      <div class="volume-row"><span class="volume">330ml</span><span class="cert-badge"></span></div>
    </div>
    <div class="pattern-band pattern-band--bottom" role="img" aria-label="Coloured band with geometric pattern"></div>
  </article>
  <article class="label label--purple">
    <div class="pattern-band" role="img" aria-label="Silver band with Zanzibar-inspired geometric pattern"></div>
    <div class="label-body">
      <div class="brand-mark"><span class="brand-mark__dot"></span>Brightfold Tamaru</div>
      <h2 class="product-name"><span>Komb</span><span>ucha</span></h2>
      <div class="taglines"><span>Feed your body</span><span>Feed your mind</span></div>
      <div class="flavour">Lemongrass</div>
      <div class="descriptor">Natural Soda</div>
      <div class="volume-row"><span class="volume">330ml</span><span class="cert-badge"></span></div>
    </div>
    <div class="pattern-band pattern-band--bottom" role="img" aria-label="Coloured band with geometric pattern"></div>
  </article>
  <article class="label label--red">
    <div class="pattern-band" role="img" aria-label="Silver band with Zanzibar-inspired geometric pattern"></div>
    <div class="label-body">
      <div class="brand-mark"><span class="brand-mark__dot"></span>Brightfold Tamaru</div>
      <h2 class="product-name"><span>Komb</span><span>ucha</span></h2>
      <div class="taglines"><span>Feed your body</span><span>Feed your mind</span></div>
      <div class="flavour">Lemongrass</div>
      <div class="descriptor">Natural Soda</div>
      <div class="volume-row"><span class="volume">330ml</span><span class="cert-badge"></span></div>
    </div>
    <div class="pattern-band pattern-band--bottom" role="img" aria-label="Coloured band with geometric pattern"></div>
  </article>
  <article class="label label--yellow">
    <div class="pattern-band" role="img" aria-label="Silver band with Zanzibar-inspired geometric pattern"></div>
    <div class="label-body">
      <div class="brand-mark"><span class="brand-mark__dot"></span>Brightfold Tamaru</div>
      <h2 class="product-name"><span>Komb</span><span>ucha</span></h2>
      <div class="taglines"><span>Feed your body</span><span>Feed your mind</span></div>
      <div class="flavour">Lemongrass</div>
      <div class="descriptor">Natural Soda</div>
      <div class="volume-row"><span class="volume">330ml</span><span class="cert-badge"></span></div>
    </div>
    <div class="pattern-band pattern-band--bottom" role="img" aria-label="Coloured band with geometric pattern"></div>
  </article>
  <article class="label label--blue">
    <div class="pattern-band" role="img" aria-label="Silver band with Zanzibar-inspired geometric pattern"></div>
    <div class="label-body">
      <div class="brand-mark"><span class="brand-mark__dot"></span>Brightfold Tamaru</div>
      <h2 class="product-name"><span>Komb</span><span>ucha</span></h2>
      <div class="taglines"><span>Feed your body</span><span>Feed your mind</span></div>
      <div class="flavour">Lemongrass</div>
      <div class="descriptor">Natural Soda</div>
      <div class="volume-row"><span class="volume">330ml</span><span class="cert-badge"></span></div>
    </div>
    <div class="pattern-band pattern-band--bottom" role="img" aria-label="Coloured band with geometric pattern"></div>
  </article>
</main>
</body>
</html>
```